Book cover design for a collection of poetry - The Lanternfield

Book cover and back design need to be moody, nostalgic, reflective, ethereal. Melancholy and other worldly. Cover design should not be time specific to a period or place but if applicable should reflect British landscape. Book cover should be in tones of blue and must include the title and author (THE LANTERNFIELD BY DORIAN WELKBRIDGE). We love the idea of rain, and looking out of a window. See attached designs. A world you are observing but not in.

Industry/Entity Type

Book Publisher

Font styles to use
Serif
Script

Colors
3176b5
3377b5
85acd3
eaf1f7
0792cd
33a6d7
86cae7
ecf7fb
86cfc6

Requirements
Must have
• The colour blue in it, must be melancholy and reflective.
Nice to have
• Rain in the cover.
Should not have
• Any bright colours.

```html
<!DOCTYPE html>
<html lang="en">
<head>
<meta charset="utf-8">
<title>The Lanternfield — Cover Spread</title>
<link rel="stylesheet" href="https://fonts.googleapis.com/css2?family=Jost:wght@400;500;600&display=swap">
<style>
  :root {
    --night: #0d1822;
    --night-deep: #070d14;
    --slate: #1c2f3d;
    --teal-dark: #143a45;
    --teal: #2e6a72;
    --teal-mist: #5f9a9c;
    --ink-white: #f4f8fa;
    --soft-white: #e6eef2;
  }
  * { margin: 0; padding: 0; box-sizing: border-box; }
  html, body { width: 1200px; height: 864px; overflow: hidden; background: var(--night); }
  .spread {
    position: relative; width: 1200px; height: 864px;
    font-family: "Jost", sans-serif; color: var(--ink-white);
  }
  .back-image {
    position: absolute; left: 0; top: 0; width: 624px; height: 864px;
    background:
      radial-gradient(ellipse at 30% 20%, rgba(60,80,95,0.55), transparent 60%),
      radial-gradient(ellipse at 70% 80%, rgba(30,50,65,0.5), transparent 60%),
      linear-gradient(180deg, var(--slate) 0%, var(--night) 55%, var(--night-deep) 100%);
  }
  .front-image {
    position: absolute; left: 624px; top: 0; width: 576px; height: 864px;
    background:
      radial-gradient(ellipse at 40% 50%, rgba(110,160,160,0.45), transparent 55%),
      linear-gradient(180deg, var(--teal-dark) 0%, var(--teal) 38%, var(--teal-mist) 52%, var(--teal) 66%, var(--teal-dark) 100%);
  }
  .divider { position: absolute; left: 150px; width: 280px; height: 20px; }
  .divider--top { top: 200px; }
  .divider--bottom { top: 605px; }
  .blurb {
    position: absolute; left: 88px; width: 440px; text-align: center;
    text-transform: uppercase; word-spacing: -0.25em;
  }
  .blurb-lead { top: 262px; font-size: 12px; font-weight: 600; letter-spacing: 0.32em; }
  .blurb-body { top: 292px; font-size: 10px; font-weight: 500; letter-spacing: 0.3em; line-height: 17px; }
  .blurb-body p + p { margin-top: 22px; }
  .spine-text {
    position: absolute; left: 600px; transform-origin: 0 0;
    transform: rotate(90deg) translateY(-50%);
    white-space: nowrap; text-transform: uppercase;
  }
  .spine-title { top: 92px; font-size: 26px; font-weight: 500; letter-spacing: 0.06em; }
  .spine-author { top: 547px; font-size: 20px; font-weight: 500; letter-spacing: 0.05em; }
  .cover-title {
    position: absolute; left: 624px; width: 576px; top: 432px;
    text-align: center; font-weight: 500; font-size: 72px; line-height: 92px;
    letter-spacing: 0.02em; text-transform: uppercase;
  }
  .cover-author {
    position: absolute; left: 624px; width: 576px; top: 650px;
    text-align: center; font-size: 20px; font-weight: 500; letter-spacing: 0.04em;
  }
</style>
</head>
<body>
<main class="spread">
  <div class="back-image" role="img" aria-label="Dark navy photograph of raindrops running down a window pane"></div>
  <div class="front-image" role="img" aria-label="Blue-teal photograph of a rainy window looking out over a misty British field with a distant farmhouse"></div>

  <svg class="divider divider--top" viewBox="0 0 280 20" aria-hidden="true">
    <line x1="30" y1="10" x2="130" y2="10" stroke="#f4f8fa" stroke-width="1.5"/>
    <circle cx="140" cy="10" r="5" fill="none" stroke="#f4f8fa" stroke-width="1.5"/>
    <line x1="150" y1="10" x2="250" y2="10" stroke="#f4f8fa" stroke-width="1.5"/>
  </svg>

  <p class="blurb blurb-lead">The Lanternfield is a collection of poetry.</p>
  <div class="blurb blurb-body">
    <p>Told in two parts we first meet Charles – aged, crippled and left alone in his inherited marsh house – reflecting on his life and his marriage to beautiful Alice who we meet in part two. Alice is suicidal, manically depressed and struggling with life as a wife and mother. She meets, harbors and falls in love with a soldier during WWII and her world is changed forever.</p>
    <p>Moving through the 20th century, this life and the next, The Lanternfield interweaves grief, loss, the after-life, mental illness, and ultimately the true nature of love.</p>
  </div>

  <svg class="divider divider--bottom" viewBox="0 0 280 20" aria-hidden="true">
    <line x1="30" y1="10" x2="130" y2="10" stroke="#f4f8fa" stroke-width="1.5"/>
    <circle cx="140" cy="10" r="5" fill="none" stroke="#f4f8fa" stroke-width="1.5"/>
    <line x1="150" y1="10" x2="250" y2="10" stroke="#f4f8fa" stroke-width="1.5"/>
  </svg>

  <p class="spine-text spine-title">The Lanternfield</p>
  <p class="spine-text spine-author">Dorian Welkbridge</p>

  <h1 class="cover-title">The<br>Lanternfield</h1>
  <p class="cover-author">DORIAN WELKBRIDGE</p>
</main>
</body>
</html>
```